RVT Event Lead Generation eFlyer

We need a brochure that highlights our Experiential Marketing and Event Management services. Using our corporate branding, images and icons, great an engaging and dynamic sales tool for our company designed to find qualified new business leads.

I would like the eFlyer in PDF format to send to clients via email, but would also like a working file (.doc) so that I can change the copy if needed.

Note: This is the first in a series of flyers. I would also eventually like to have printed versions, but for now I'm only doing electronic. My company offers 3 services: 1. Business Development; 2. Marketing Communications (this is the flyer you are working on); 3. Keynotes, i.e. motivational speaking. I will be producing a flyer for each of those services. The branding will be similar but the messaging will have a focus on the specific service.
Updates

Project Deadline Extended
Reason: I'm using this first experience with Pixel Harbor as a test. I'm looking for an affordable solution for ongoing design work. I would like to see more options coming in so that I can not only choose a great flyer, but can also choose a long term designer.

Target Market(s)

Marketing and Advertising Agencies, Production Companies

Industry/Entity Type

Marketing

Colors
e667a6
5c5c5c

Requirements
Must have
• Would like it to be clear, simple and inspiring. I want them to call me to discuss a project.
Nice to have
• Can convert copy to info graphs, I would like it to be visual and easy for someone to scan and get the information quickly.
Should not have
• I don't want it to be copy heavy.

```html
<!DOCTYPE html>
<html lang="en">
<head>
<meta charset="utf-8">
<title>RVT Event Group – Experiential Marketing & Event Management eFlyer</title>
<link href="https://fonts.googleapis.com/css2?family=Raleway:wght@400;500;600;700;800&display=swap" rel="stylesheet">
<style>
  :root {
    --magenta: #d6246e;
    --charcoal: #454545;
    --graphite: #3f3f3f;
    --ink: #4a4a4a;
    --mist: #ececec;
    --paper: #ffffff;
    --backdrop: #e2e2e2;
  }
  * { box-sizing: border-box; margin: 0; padding: 0; }
  html, body { width: 1200px; height: 1200px; overflow: hidden; }
  body { background: var(--backdrop); font-family: "Raleway", sans-serif; color: var(--ink); position: relative; font-variant-numeric: lining-nums; }

  .flyer { position: absolute; left: 205px; top: 46px; width: 790px; height: 1108px; background: var(--paper); overflow: hidden; }
  .flyer > * { position: absolute; }

  .hero-photo { left: 0; top: 0; width: 790px; height: 400px;
    background: linear-gradient(100deg, #111 0%, #3a3a3a 35%, #bdbdbd 60%, #f0f0f0 80%, #dcdcdc 100%); }
  .hero-panel { left: 0; top: 137px; width: 530px; height: 263px;
    background: linear-gradient(90deg, rgba(160,160,160,.92) 0%, rgba(170,170,170,.85) 75%, rgba(170,170,170,0) 100%); }
  .hero-title { left: 42px; top: 184px; font-size: 33px; font-weight: 800; line-height: 1.17; color: var(--ink); letter-spacing: -0.5px; }
  .hero-lede { left: 42px; top: 262px; font-size: 23.5px; font-weight: 500; line-height: 1.3; color: var(--ink); width: 400px; }
  .hero-lede strong { font-weight: 800; }

  .brand { left: 560px; top: 96px; font-size: 20px; font-weight: 700; letter-spacing: 1px; color: var(--charcoal); text-transform: uppercase; white-space: nowrap; }

  .pitch-band { left: 0; top: 400px; width: 790px; height: 78px; background: var(--magenta); color: #fff;
    font-size: 17.5px; font-weight: 700; line-height: 1.33; padding: 18px 42px 0; }

  .services { left: 0; top: 478px; width: 790px; height: 208px; }
  .service-col { position: absolute; top: 20px; list-style: none; }
  .service-col li { display: flex; align-items: flex-start; gap: 8px; font-size: 14.2px; line-height: 1.35; color: var(--charcoal); margin-bottom: 11px; }
  .service-col li svg { flex: none; width: 19px; height: 19px; }
  .col-a { left: 42px; } .col-b { left: 295px; } .col-c { left: 547px; }
  .col-b li, .col-c li { margin-bottom: 12px; }
  .col-rule { position: absolute; top: 22px; width: 1px; height: 170px; background: linear-gradient(#fff, #ccc, #fff); }

  .strengths { left: 0; top: 686px; width: 790px; height: 192px; background: var(--mist); }
  .strengths-intro { position: absolute; left: 42px; top: 14px; width: 700px; font-size: 15px; font-weight: 700; line-height: 1.3; color: var(--graphite); }
  .strength { position: absolute; display: flex; align-items: center; gap: 10px; font-size: 19.5px; font-weight: 700; line-height: 1.17; color: var(--ink); }
  .strength-icon { width: 43px; height: 43px; border-radius: 50%; background: var(--magenta); display: flex; align-items: center; justify-content: center; flex: none; }
  .strength-icon svg { width: 26px; height: 26px; }
  .strength-rule { position: absolute; top: 66px; width: 1px; height: 112px; background: linear-gradient(#ececec, #c8c8c8, #ececec); }

  .team-note { left: 200px; top: 912px; width: 560px; font-size: 14.4px; font-weight: 700; line-height: 1.35; color: var(--graphite); text-transform: uppercase; }

  .contact-bar { left: 0; top: 976px; width: 790px; height: 132px; background: var(--charcoal); }
  .contact-tab { position: absolute; left: 264px; top: 0; width: 409px; height: 30px; background: var(--paper);
    clip-path: polygon(0 0, 100% 0, 94% 100%, 6% 100%); font-size: 15px; font-weight: 700; color: var(--graphite); text-align: center; line-height: 28px; }
  .contact-name { position: absolute; left: 200px; top: 45px; display: flex; align-items: center; gap: 6px; color: #fff; font-size: 22px; white-space: nowrap; }
  .contact-name b { font-weight: 800; }
  .contact-name .role { font-weight: 400; margin-right: 10px; }
  .contact-lines { position: absolute; left: 210px; top: 78px; display: flex; align-items: center; gap: 6px; color: #fff; font-size: 15.5px; white-space: nowrap; }
  .contact-lines .gap { width: 10px; }
  .contact-bar svg { flex: none; }

  .portrait { left: 44px; top: 895px; width: 143px; height: 169px; border-radius: 14px;
    background: linear-gradient(160deg, #c9c4ba 0%, #e4d6c2 45%, #b9ada0 100%); }
</style>
</head>
<body>
<main class="flyer">
  <div class="hero-photo" role="img" aria-label="Businessman balancing on a tightrope that unravels from a tangle of black scribbled lines"></div>
  <div class="hero-panel"></div>

  <div class="brand">RVT Event Group</div>

  <h1 class="hero-title">EXPERIENTIAL MARKETING<br>&amp; EVENT MANAGEMENT</h1>
  <p class="hero-lede">We offer agencies white label solutions. Need to fill a gap in a hurry with no time to hire?<br><strong>We can help!</strong></p>

  <p class="pitch-band">Our team plugs in and ramps up, to quickly deliver critical solutions that make a big impact on your business!&nbsp; Our services include:</p>

  <section class="services">
    <ul class="service-col col-a">
      <li><svg viewBox="0 0 20 20"><circle cx="10" cy="9" r="5" fill="none" stroke="#d6246e" stroke-width="1.6"/><rect x="8" y="14" width="4" height="4" fill="#d6246e"/></svg>Ideation &amp; Concept<br>Development</li>
      <li><svg viewBox="0 0 20 20"><circle cx="10" cy="10" r="6" fill="#d6246e"/><circle cx="10" cy="10" r="2" fill="#fff"/></svg>Strategic Planning</li>
      <li><svg viewBox="0 0 20 20"><rect x="2" y="3" width="14" height="12" fill="none" stroke="#d6246e" stroke-width="1.6"/><circle cx="14" cy="13" r="3" fill="none" stroke="#d6246e" stroke-width="1.6"/></svg>Research &amp; Feasibility</li>
      <li><svg viewBox="0 0 20 20"><rect x="2" y="3" width="16" height="15" fill="none" stroke="#d6246e" stroke-width="1.6"/><path d="M2 7h16M7 7v11M12 7v11M2 12h16" stroke="#d6246e"/></svg>Event Creation &amp; Logistics</li>
      <li><svg viewBox="0 0 20 20"><path d="M10 2a5 5 0 0 1 5 5c0 4-5 8-5 8s-5-4-5-8a5 5 0 0 1 5-5z" fill="none" stroke="#d6246e" stroke-width="1.6"/><path d="M2 18h16" stroke="#d6246e" stroke-width="1.6"/></svg>Venue, Permit and<br>Supplier Negotiations</li>
    </ul>
    <span class="col-rule" style="left:271px"></span>
    <ul class="service-col col-b">
      <li><svg viewBox="0 0 20 20"><circle cx="8" cy="6" r="4" fill="#d6246e"/><path d="M1 18c0-5 4-7 7-7s5 1 6 3" fill="#d6246e"/><circle cx="15" cy="15" r="3" fill="#d6246e"/></svg>Registration Management</li>
      <li><svg viewBox="0 0 20 20"><path d="M2 15a8 8 0 0 1 16 0z" fill="#d6246e"/><rect x="1" y="16" width="18" height="2" fill="#d6246e"/></svg>Hospitality</li>
      <li><svg viewBox="0 0 20 20"><rect x="12" y="4" width="5" height="14" fill="#d6246e"/><path d="M2 11h9M2 14h9M2 17h9" stroke="#d6246e" stroke-width="2"/></svg>Food &amp; Beverage</li>
      <li><svg viewBox="0 0 20 20"><path d="M3 3l14 14M17 3L3 17" stroke="#d6246e" stroke-width="2.4"/></svg>Design &amp; Décor</li>
      <li><svg viewBox="0 0 20 20"><circle cx="6" cy="13" r="4" fill="none" stroke="#d6246e" stroke-width="2"/><circle cx="14" cy="13" r="4" fill="none" stroke="#d6246e" stroke-width="2"/><circle cx="10" cy="5" r="3.5" fill="none" stroke="#d6246e" stroke-width="2"/></svg>Full Production Services</li>
      <li><svg viewBox="0 0 20 20"><rect x="2" y="5" width="16" height="12" fill="#d6246e"/><circle cx="10" cy="11" r="3.5" fill="#fff"/></svg>A/V, Lighting &amp; Sound</li>
    </ul>
    <span class="col-rule" style="left:522px"></span>
    <ul class="service-col col-c">
      <li><svg viewBox="0 0 20 20"><circle cx="10" cy="9" r="5" fill="#d6246e"/><rect x="8" y="14" width="4" height="4" fill="#d6246e"/><path d="M10 1v2M2 9h2M16 9h2" stroke="#d6246e" stroke-width="1.4"/></svg>Creative Services</li>
      <li><svg viewBox="0 0 20 20"><rect x="3" y="5" width="14" height="10" fill="none" stroke="#d6246e" stroke-width="1.6"/><path d="M1 17h18" stroke="#d6246e" stroke-width="2"/></svg>Technology Management</li>
      <li><svg viewBox="0 0 20 20"><circle cx="10" cy="10" r="7" fill="#d6246e"/><path d="M3 12c5-1 9-4 15-8" stroke="#fff" stroke-width="1.6" fill="none"/></svg>Travel Logistics</li>
      <li><svg viewBox="0 0 20 20"><circle cx="7" cy="5" r="3" fill="#d6246e"/><path d="M2 18v-6c0-2 2-3 5-3s5 1 5 3v6z" fill="#d6246e"/><rect x="12" y="12" width="7" height="6" fill="#d6246e"/></svg>Speaker Management</li>
      <li><svg viewBox="0 0 20 20"><circle cx="10" cy="6" r="3.5" fill="#d6246e"/><path d="M4 15c0-4 3-5 6-5s6 1 6 5z" fill="#d6246e"/><path d="M1 17h18" stroke="#d6246e" stroke-width="1.6"/></svg>Delegate Management</li>
      <li><svg viewBox="0 0 20 20"><rect x="3" y="3" width="14" height="10" fill="none" stroke="#d6246e" stroke-width="1.6"/><path d="M6 13v6M14 13v6" stroke="#d6246e" stroke-width="1.6"/></svg>On-site Management</li>
    </ul>
  </section>

  <section class="strengths">
    <p class="strengths-intro">We can help! Tap into our service for short or long term support. Our team is ready to jump in and make an impact on your business.</p>
    <div class="strength" style="left:44px;top:64px"><span class="strength-icon"><svg viewBox="0 0 26 26"><circle cx="7" cy="8" r="3" fill="#fff"/><circle cx="13" cy="6" r="3" fill="#fff"/><circle cx="19" cy="8" r="3" fill="#fff"/><rect x="4" y="12" width="6" height="10" fill="#fff"/><rect x="10" y="10" width="6" height="12" fill="#fff"/><rect x="16" y="12" width="6" height="10" fill="#fff"/></svg></span>Senior<br>Leadership</div>
    <div class="strength" style="left:44px;top:132px"><span class="strength-icon"><svg viewBox="0 0 26 26"><circle cx="8" cy="7" r="3" fill="#fff"/><circle cx="18" cy="7" r="3" fill="#fff"/><rect x="5" y="11" width="6" height="11" fill="#fff"/><rect x="15" y="11" width="6" height="11" fill="#fff"/><path d="M11 14h4" stroke="#fff" stroke-width="2"/></svg></span>Collaborative<br>Mindset</div>
    <span class="strength-rule" style="left:268px"></span>
    <div class="strength" style="left:307px;top:64px"><span class="strength-icon"><svg viewBox="0 0 26 26"><path d="M2 13c4-6 18-6 22 0c-4 6-18 6-22 0z" fill="#fff"/><circle cx="13" cy="13" r="4" fill="#d6246e"/><circle cx="13" cy="13" r="1.6" fill="#fff"/></svg></span>Modern<br>Perspective</div>
    <div class="strength" style="left:307px;top:132px"><span class="strength-icon"><svg viewBox="0 0 26 26"><rect x="5" y="3" width="14" height="19" rx="2" fill="none" stroke="#fff" stroke-width="2"/><circle cx="15" cy="15" r="4" fill="none" stroke="#fff" stroke-width="2"/></svg></span>Practical<br>Tools</div>
    <span class="strength-rule" style="left:530px"></span>
    <div class="strength" style="left:570px;top:64px"><span class="strength-icon"><svg viewBox="0 0 26 26"><circle cx="13" cy="12" r="3" fill="#fff"/><path d="M8 24v-6c0-2 2-3 5-3s5 1 5 3v6z" fill="#fff"/><circle cx="5" cy="5" r="2" fill="none" stroke="#fff" stroke-width="1.4"/><rect x="11" y="2" width="4" height="4" fill="none" stroke="#fff" stroke-width="1.4"/><path d="M21 3l2 4h-4z" fill="none" stroke="#fff" stroke-width="1.4"/></svg></span>Depth of<br>Perspective</div>
    <div class="strength" style="left:570px;top:132px"><span class="strength-icon"><svg viewBox="0 0 26 26"><circle cx="13" cy="14" r="9" fill="none" stroke="#fff" stroke-width="2"/><circle cx="13" cy="14" r="5" fill="none" stroke="#fff" stroke-width="2"/><circle cx="13" cy="14" r="1.6" fill="#fff"/><path d="M13 14L22 4" stroke="#fff" stroke-width="2"/></svg></span>Goal<br>Oriented</div>
  </section>

  <p class="team-note">The RVT team is composed of highly motivated experts who are focused on delivering flawless and impactful results for you!</p>

  <section class="contact-bar">
    <div class="contact-tab">Call me personally to discuss your challenge:</div>
    <div class="contact-name">
      <svg width="20" height="20" viewBox="0 0 20 20"><circle cx="10" cy="10" r="9" fill="none" stroke="#fff" stroke-width="1.6"/><circle cx="10" cy="8" r="3" fill="#fff"/><path d="M5 16c1-3 3-4 5-4s4 1 5 4" fill="#fff"/></svg>
      <span><b>CLAIRE DAWSON</b><span class="role">, PRESIDENT</span></span>
      <svg width="20" height="20" viewBox="0 0 20 20"><circle cx="10" cy="10" r="9" fill="none" stroke="#fff" stroke-width="1.6"/><rect x="7" y="4" width="6" height="12" rx="1" fill="none" stroke="#fff" stroke-width="1.6"/></svg>
      <b>(555) 010-4827</b>
    </div>
    <div class="contact-lines">
      <svg width="18" height="18" viewBox="0 0 20 20"><circle cx="10" cy="10" r="9" fill="none" stroke="#fff" stroke-width="1.4"/><rect x="5" y="6.5" width="10" height="7" fill="none" stroke="#fff" stroke-width="1.3"/><path d="M5 7l5 4 5-4" fill="none" stroke="#fff" stroke-width="1.3"/></svg>
      <span>claire@rvtstrategic.com</span><span class="gap"></span>
      <svg width="18" height="18" viewBox="0 0 20 20"><circle cx="10" cy="10" r="9" fill="none" stroke="#fff" stroke-width="1.4"/><circle cx="10" cy="10" r="5" fill="none" stroke="#fff" stroke-width="1.3"/><path d="M5 10h10M10 5v10" stroke="#fff" stroke-width="1.1"/></svg>
      <span>rvtstrategic.com</span>
    </div>
  </section>

  <div class="portrait" role="img" aria-label="Portrait photo of the company president"></div>
</main>
</body>
</html>
```